Aged Care Consultancy Business needs a business card design

I need a two sided business card - I want it clean and professional. Surprise me

Target Market(s)

middle aged and ageing victorians

Industry/Entity Type

Health Care

Contact Information for Business Card

Text to be included

Logo
Aged Care Consulting Services
Professional, Reliable, Affordable

Tovan Brelsick
Director
0427 31 64 92 (larger)
1300 73 29 41
tovan@wadolire.com.au
www.wadolcare.com.au
Facebook (details TBA)

include little icons beside the contact info:

- Envelope = email
- Phone = phone
- Globe = website

Font styles to use
Serif
Sans Serif

Requirements
Must have
• look proffesional and clean

```html
<!DOCTYPE html>
<html lang="en">
<head>
<meta charset="utf-8">
<title>Wadol Care – Business Card</title>
<link rel="stylesheet" href="https://fonts.googleapis.com/css2?family=Montserrat:wght@300;400;600;700&display=swap">
<style>
  :root {
    --navy: #1f3f7a;
    --orange: #f2891f;
    --paper: #ffffff;
    --backdrop: #c9c9cb;
    --muted: #5a6a8a;
  }
  * { box-sizing: border-box; margin: 0; padding: 0; }
  html, body { width: 1200px; height: 960px; overflow: hidden; }
  body {
    background: var(--backdrop);
    font-family: "Montserrat", Arial, sans-serif;
    color: var(--navy);
    display: flex; flex-direction: column; align-items: center; justify-content: center;
    gap: 44px;
  }
  .card {
    position: relative;
    width: 700px; height: 400px;
    background: var(--paper);
    box-shadow: 0 6px 18px rgba(0,0,0,.18);
  }

  /* Front */
  .front__band { position: absolute; left: 0; right: 0; height: 38px; background: var(--orange); }
  .front__band--top { top: 0; }
  .front__band--bottom { bottom: 0; }
  .front__rules { position: absolute; left: 0; right: 0; height: 16px; }
  .front__rules--top { top: 44px; }
  .front__rules--bottom { bottom: 44px; }
  .front__rules span { display: block; height: 2px; background: var(--navy); margin-bottom: 4px; }
  .front__body {
    position: absolute; inset: 60px 0; display: flex; flex-direction: column;
    align-items: center; justify-content: center; text-align: center;
  }
  .brand { display: flex; align-items: center; gap: 12px; }
  .brand__dot { width: 22px; height: 22px; border-radius: 50%; background: var(--orange); }
  .brand__name { font-weight: 700; color: var(--navy); letter-spacing: .5px; }
  .front .brand__name { font-size: 58px; line-height: 1; }
  .front .brand__dot { width: 34px; height: 34px; }
  .front__services { font-weight: 400; font-size: 17px; letter-spacing: .8px; margin-top: 10px; }
  .front__tagline { font-weight: 700; font-size: 22px; letter-spacing: 1px; margin-top: 30px; }

  /* Back */
  .back { border: 14px solid var(--orange); }
  .back .brand { position: absolute; top: 30px; right: 36px; }
  .back .brand__name { font-size: 30px; }
  .back .brand__dot { width: 18px; height: 18px; }
  .person { position: absolute; left: 40px; top: 140px; display: flex; gap: 12px; align-items: flex-start; }
  .person__icon { width: 32px; height: 32px; }
  .person__name { font-weight: 700; font-size: 22px; text-transform: uppercase; letter-spacing: .3px; }
  .person__role { font-weight: 600; font-size: 15px; color: var(--orange); text-transform: uppercase; }
  .contacts { position: absolute; left: 40px; bottom: 32px; list-style: none; }
  .contacts li { display: flex; align-items: center; gap: 12px; margin-top: 12px; font-size: 16px; font-weight: 600; }
  .contacts .phone__main { font-size: 24px; font-weight: 700; line-height: 1; }
  .contacts .phone__alt { font-size: 14px; font-weight: 300; color: var(--muted); }
  .icon { width: 28px; height: 28px; border-radius: 5px; background: var(--orange); flex: none; display: grid; place-items: center; }
  .icon svg { width: 17px; height: 17px; }
  .divider { position: absolute; left: 382px; top: 180px; width: 2px; height: 150px; background: var(--orange); }
  .social { position: absolute; left: 404px; top: 186px; list-style: none; }
  .social li { display: flex; align-items: center; gap: 14px; font-size: 15px; font-weight: 600; margin-bottom: 22px; }
  .social__mark { width: 26px; height: 26px; border-radius: 4px; background: var(--orange); flex: none; }
</style>
</head>
<body>

<section class="card front" aria-label="Card front">
  <div class="front__band front__band--top"></div>
  <div class="front__rules front__rules--top"><span></span><span></span><span></span></div>
  <div class="front__body">
    <div class="brand"><span class="brand__dot"></span><span class="brand__name">wadol care</span></div>
    <p class="front__services">AGED CARE CONSULTING SERVICES</p>
    <p class="front__tagline">PROFESSIONAL, RELIABLE, AFFORDABLE</p>
  </div>
  <div class="front__rules front__rules--bottom"><span></span><span></span><span></span></div>
  <div class="front__band front__band--bottom"></div>
</section>

<section class="card back" aria-label="Card back">
  <div class="brand"><span class="brand__dot"></span><span class="brand__name">wadol care</span></div>

  <div class="person">
    <svg class="person__icon" viewBox="0 0 32 32" aria-hidden="true">
      <circle cx="16" cy="16" r="14" fill="none" stroke="var(--orange)" stroke-width="3"/>
      <circle cx="16" cy="13" r="5" fill="var(--orange)"/>
      <path d="M7 25c2-5 16-5 18 0" fill="var(--orange)"/>
    </svg>
    <div>
      <p class="person__name">Tovan Brelsick</p>
      <p class="person__role">Director</p>
    </div>
  </div>

  <ul class="contacts">
    <li>
      <span class="icon"><svg viewBox="0 0 24 24" aria-hidden="true"><path d="M6 3l3 0 2 5-2 1.5a11 11 0 0 0 5.5 5.5L16 13l5 2v3a2 2 0 0 1-2 2A17 17 0 0 1 4 5a2 2 0 0 1 2-2z" fill="#fff"/></svg></span>
      <div><p class="phone__main">0427 31 64 92</p><p class="phone__alt">(1300 73 29 41)</p></div>
    </li>
    <li>
      <span class="icon"><svg viewBox="0 0 24 24" aria-hidden="true"><rect x="3" y="6" width="18" height="13" rx="1" fill="none" stroke="#fff" stroke-width="2"/><path d="M3 7l9 7 9-7" fill="none" stroke="#fff" stroke-width="2"/></svg></span>
      <span>tovan@wadolire.com.au</span>
    </li>
    <li>
      <span class="icon"><svg viewBox="0 0 24 24" aria-hidden="true"><g fill="none" stroke="#fff" stroke-width="1.8"><circle cx="12" cy="12" r="9"/><ellipse cx="12" cy="12" rx="4" ry="9"/><path d="M3 12h18M5 7h14M5 17h14"/></g></svg></span>
      <span>www.wadolcare.com.au</span>
    </li>
  </ul>

  <div class="divider"></div>

  <ul class="social">
    <li><span class="social__mark"></span><span>tovan@wadolire.com.au</span></li>
    <li><span class="social__mark"></span><span>tovan@wadolire.com.au</span></li>
    <li><span class="social__mark"></span><span>tovan@wadolire.com.au</span></li>
  </ul>
</section>

</body>
</html>
```